The Willow Cove Clinic - Instagram Photospot

We are looking for an instagram type wal for our pediatric dental office. We are thinking it could be weaved into a whole bunch of what we do (i.e. potentially water marked or faded in the background on letterhead, as an instragram type wall in the practice, as a banner or section of the home page on the website, on rack cards, etc.) I’m thinking it would utilize a nice fun cursive script for the wording "The Willow Cove Clinic is the spot for...." and a bunch of different sized “spots” with meaningful words that speak to who we are. That list would include things like:

• Fun
• Smiles
• Laughter
• Caring
• Comfort
• Amazing
• Kids
• Toddlers
• Teens
• Friends
• Family
• Health
• Education
• Cheer
• Positivity
• Exceptional Care

From a color perspective….we could look at a couple of options. We could have one version that has it washed out and in the background (more subliminal). We could have one version that was consistent with the colors in our logo. And we could have one version that popped with more color by utilizing the colors in some of the artwork we use throughout the office (snowboard picture as an example)

Target Market(s)

Appeal to hip families with kids

Industry/Entity Type

Pediatric Dental

Other font styles liked:
• something modern, hip, playful and fun

Colors
0054AA
0677BA
7BADD7
CADEEF
E8F1F8
0094D4
00A9DD
6FCCEA
C7EBF8
E9F6FB
00AB8E
00BBA5
67D7C9
C6EFE9
E9F9F6

Requirements
Must have
• Use of existing logo and a play on "spots" or polka dots with symbpolic wording. Must appeal to young parents and kiddos (including hip teens)
Should not have
• SHOULDNT BE OVER THE TOP KIDS.

```html
<!DOCTYPE html>
<html lang="en">
<head>
<meta charset="utf-8">
<title>The Willow Cove Clinic is the spot for....</title>
<link rel="stylesheet" href="https://fonts.googleapis.com/css2?family=Nunito:wght@800;900&family=Yellowtail&display=swap">
<style>
  :root {
    --paper: #dfe6ed;
    --paper-edge: #d3dce5;
    --ink: #16384a;
    --navy-spot: #173a4e;
    --blue-deep: #0677ba;
    --blue-mid: #7badd7;
    --blue-pale: #cde2f2;
    --mint-pale: #cdeaea;
    --teal: #12a98c;
    --script-ink: #1c4f9c;
    --white: #ffffff;
    --shadow: rgba(120, 110, 190, 0.28);
  }
  * { box-sizing: border-box; margin: 0; padding: 0; }
  html, body { width: 1200px; height: 849px; overflow: hidden; }
  body { background: var(--paper); }
  .canvas {
    position: relative;
    width: 1200px;
    height: 849px;
    overflow: hidden;
    background: radial-gradient(ellipse at 50% 45%, #e7edf2 0%, var(--paper) 60%, var(--paper-edge) 100%);
  }
  .headline-band { position: absolute; left: 165px; top: 48px; width: 880px; height: 90px; }
  .headline {
    position: absolute; left: 165px; top: 48px; width: 880px; height: 90px;
    display: flex; align-items: center; justify-content: center;
    font-family: "Nunito", sans-serif; font-weight: 900;
    font-size: 31px; letter-spacing: 0.5px; color: var(--white);
  }
  .spot {
    position: absolute;
    border-radius: 50%;
    display: flex; align-items: center; justify-content: center;
    text-align: center;
    font-family: "Yellowtail", cursive;
    line-height: 1.05;
    box-shadow: 4px 6px 10px var(--shadow);
    transform: translate(-50%, -50%);
  }
  .spot--deep { background: var(--blue-deep); color: var(--white); }
  .spot--mid { background: var(--blue-mid); color: var(--white); }
  .spot--teal { background: var(--teal); color: var(--white); }
  .spot--pale { background: var(--blue-pale); color: var(--script-ink); }
  .spot--mint { background: var(--mint-pale); color: var(--script-ink); }

  .hub {
    position: absolute; left: 594px; top: 452px;
    width: 456px; height: 456px; border-radius: 50%;
    transform: translate(-50%, -50%);
    background: var(--navy-spot);
    box-shadow: 4px 8px 14px var(--shadow);
  }
  .hub-art {
    position: absolute; left: 455px; top: 355px; width: 290px; height: 190px;
    border-radius: 40px;
    background: radial-gradient(ellipse at 50% 50%, #c9e2f2 0%, #9cc6e3 70%, rgba(156,198,227,0.0) 100%);
  }
  .hub-place {
    position: absolute; left: 594px; top: 606px;
    transform: translate(-50%, -50%);
    font-family: "Nunito", sans-serif; font-weight: 900;
    font-size: 26px; letter-spacing: 1px; color: var(--white); white-space: nowrap;
  }
</style>
</head>
<body>
<main class="canvas">
  <svg class="headline-band" viewBox="0 0 880 90" preserveAspectRatio="none" aria-hidden="true">
    <path fill="var(--ink)" d="M14 8 L120 4 L300 10 L520 3 L720 9 L866 5 L852 20 L874 30 L858 44 L878 58 L860 70 L872 84 L700 82 L480 88 L260 81 L60 86 L10 82 L24 70 L4 58 L20 46 L2 34 L22 22 Z"/>
  </svg>
  <h1 class="headline">The Willow Cove Clinic is the spot for....</h1>

  <div class="hub"></div>
  <div class="hub-art" role="img" aria-label="Light blue watercolour illustration of a walking bear with a small star above it"></div>
  <p class="hub-place">MAPLE HOLLOW, CA</p>

  <div class="spot spot--deep" style="left:185px;top:259px;width:170px;height:170px;font-size:40px;">Amazing</div>
  <div class="spot spot--pale" style="left:423px;top:268px;width:128px;height:128px;font-size:27px;">Amazing</div>
  <div class="spot spot--teal" style="left:282px;top:393px;width:96px;height:96px;font-size:21px;">Toddlers</div>
  <div class="spot spot--mid" style="left:135px;top:430px;width:108px;height:108px;font-size:34px;">Smile</div>
  <div class="spot spot--mint" style="left:274px;top:546px;width:148px;height:148px;font-size:36px;">Comfort</div>
  <div class="spot spot--deep" style="left:125px;top:607px;width:86px;height:86px;font-size:23px;">Cheer</div>
  <div class="spot spot--mid" style="left:235px;top:727px;width:122px;height:122px;font-size:33px;">Caring</div>
  <div class="spot spot--pale" style="left:435px;top:734px;width:162px;height:162px;font-size:29px;">Exceptional<br>Care</div>
  <div class="spot spot--mint" style="left:738px;top:296px;width:108px;height:108px;font-size:38px;">Fun</div>
  <div class="spot spot--teal" style="left:886px;top:304px;width:108px;height:108px;font-size:34px;">Teens</div>
  <div class="spot spot--pale" style="left:1037px;top:259px;width:116px;height:116px;font-size:23px;">Positivity</div>
  <div class="spot spot--mid" style="left:1077px;top:423px;width:166px;height:166px;font-size:32px;">Education</div>
  <div class="spot spot--deep" style="left:881px;top:494px;width:154px;height:154px;font-size:40px;">Health</div>
  <div class="spot spot--teal" style="left:1089px;top:590px;width:94px;height:94px;font-size:23px;">Friends</div>
  <div class="spot spot--teal" style="left:805px;top:660px;width:76px;height:76px;font-size:25px;">Kids</div>
  <div class="spot spot--pale" style="left:966px;top:698px;width:162px;height:162px;font-size:44px;">Family</div>
</main>
</body>
</html>
```